Prairie Lantern Pantry Farm-to-Table Restaurant Menu

We are a farm-to-table restaurant. We grow all of our natural raised and finished grass-fed beef. No hormones or antibiotics ever. We try and source many of our products locally as well. We also sell Kansas products and our meats and Kansas cheeses and butters in our restaurant. It's almost like a Hearth Kettle setting. Our restaurant is on main street in an old drug store from the 1920s. It features an old-soda fountain so we make all of our drinks and shakes, malts by hand. I need help re-designing my menu plus I want to add some items.
I would like one side to be the breakfast menu and the other side to be the lunch and supper menu. I would also like to create a separate drink/dessert menu.
I need to add some more items as well.

Target Market(s)

Farmers, Cowboys, Rural community less than 1200 people in town, regenerative & sustainability conscience

Industry/Entity Type

Ag

Font styles to use
Sans Serif

Colors
0054AA
0677BA
7BADD7
CADEEF
E8F1F8
0094D4
00A9DD
6FCCEA
C7EBF8
E9F6FB
00AB8E
00BBA5
67D7C9
C6EFE9
E9F9F6
FFF300
FFF600
FEFA6F
FFFEC7
FFFEE8
FFC000
F8CF3A
FAE287
FDF2CF
FEFAEE
EB3D1F
EC4F4E
F09395
F8D3D4
FCEDEE

Requirements
Must have
• Clean lines-easy to read prices-help with food descriptions
Nice to have
• Like to incorporate some of our story if there is room.

```html
<!DOCTYPE html>
<html lang="en">
<head>
<meta charset="utf-8">
<title>Prairie Lantern Pantry – Menu</title>
<link rel="stylesheet" href="https://fonts.googleapis.com/css2?family=Graduate&family=Montserrat:wght@700;800&family=Roboto+Condensed:wght@400;700&family=Rye&family=Lobster&display=swap">
<style>
:root{
  --stage:#a9a9a9;
  --red:#e1232b;
  --aqua:#acdad4;
  --ink:#0d0d0d;
  --white:#ffffff;
  --teal-text:#2d9a8b;
  --photo-green:#7a9a58;
}
*{box-sizing:border-box;margin:0;padding:0}
html,body{width:834px;height:1200px;overflow:hidden;background:var(--stage)}
body{position:relative;font-family:"Roboto Condensed",Arial,sans-serif;color:var(--ink)}
.page{position:absolute;width:358px;height:464px;overflow:hidden;box-shadow:0 2px 6px rgba(0,0,0,.35)}
.page--breakfast{left:50px;top:117px;background:var(--aqua)}
.page--lunch{left:427px;top:117px;background:var(--ink)}
.page--burgers{left:50px;top:613px;background:var(--ink)}
.page--drinks{left:427px;top:613px;background:var(--aqua)}
.abs{position:absolute}
.wave{position:absolute;left:0;top:0;width:358px;height:90px}
.brand{position:absolute;width:74px;height:74px;border-radius:50%;background:var(--aqua);border:3px solid var(--ink);display:flex;align-items:center;justify-content:center;text-align:center;font-family:"Montserrat",sans-serif;font-weight:800;font-size:9px;line-height:1.1;color:var(--ink);padding:6px;z-index:2}
.photo{position:absolute;border-radius:50%;border:2px dotted var(--white)}
.photo--breakfast{border-color:var(--red);background:radial-gradient(circle at 50% 40%,#f1d36a,#a8633a 70%)}
.footer{position:absolute;left:14px;top:443px;width:331px;height:19px;border-radius:10px 10px 0 0;font-family:"Montserrat",sans-serif;font-weight:700;font-size:6.6px;display:flex;align-items:center;justify-content:center;gap:4px}
.footer--dark{background:var(--ink);color:var(--white)}
.footer--light{background:var(--white);color:var(--ink)}
.footer .sep{color:var(--red)}
.footer .phone{color:var(--red)}
.item{margin-bottom:4px}
.item h4{display:flex;justify-content:space-between;font-family:"Montserrat",sans-serif;font-weight:700;font-size:6.4px;line-height:1.15}
.item h4 b{font-weight:700;margin-left:6px}
.item p{font-size:4.6px;line-height:1.2;padding-right:22px}
.on-red{color:var(--white)}
.on-dark{color:var(--white)}
.on-dark .item h4{color:var(--white)}
.title-box{position:absolute;background:var(--white);border:1.5px solid var(--red);font-family:"Graduate",serif;text-align:center;color:var(--ink)}
.section-side{font-family:"Montserrat",sans-serif;font-weight:800;font-size:9.6px;color:var(--white)}
.mini{position:absolute}
.mini table{border-collapse:collapse;font-family:"Montserrat",sans-serif;font-weight:700;font-size:5.4px}
.mini td{padding:0 0 .3px}
.mini td:last-child{text-align:right;padding-left:6px}
.vlabel{position:absolute;font-family:"Montserrat",sans-serif;font-weight:800;color:var(--white);background:var(--red);writing-mode:vertical-rl;transform:rotate(180deg);text-align:center;display:flex;align-items:center;justify-content:center}
.drink-list{font-family:"Montserrat",sans-serif;font-weight:700;font-size:5.1px;line-height:1.27}
.drink-list .row{display:flex;justify-content:space-between}
.drink-list .row span:first-child{max-width:110px}
.burger-heading{position:absolute;left:24px;top:44px;font-family:"Graduate",serif;line-height:1;z-index:1}
.story-label{position:absolute;left:-9px;top:375px;width:66px;height:16px;transform:rotate(-94deg);font-family:"Graduate",serif;font-size:8.4px;line-height:16px;color:var(--white);text-align:center;white-space:nowrap}
</style>
</head>
<body>

<!-- Breakfast page -->
<section class="page page--breakfast">
  <div class="abs" style="left:0;top:36px;width:139px;height:428px;background:var(--red)"></div>
  <svg class="wave" viewBox="0 0 358 90" aria-hidden="true">
    <path d="M0 0H358V34C290 46 220 22 150 44C95 60 40 52 0 48Z" fill="var(--white)"/>
    <path d="M0 48C40 52 95 60 150 44C220 22 290 46 358 34V40C290 52 220 30 150 50C95 66 40 58 0 56Z" fill="var(--ink)"/>
  </svg>
  <div class="brand" style="left:22px;top:4px">Prairie Lantern Pantry</div>
  <div class="photo photo--breakfast" style="left:210px;top:34px;width:70px;height:70px" role="img" aria-label="Photo of scrambled eggs with avocado and bacon"></div>

  <div class="abs on-red" style="left:14px;top:86px;width:116px">
    <div class="section-side" style="margin-bottom:6px">THE LIGHTER SIDE</div>
    <div class="item"><h4>Breakfast Sandwich<b>7.25</b></h4><p>Sausage or bacon, fried egg, and cheese sandwiched between a buttermilk biscuit, croissant, English muffin, or toast.<br>Add Avocado +$2.75</p></div>
    <div class="item"><h4>Avocado Toast<b>7.25</b></h4><p>Avocado mash with cherry tomatoes served on top of toast sprinkled with olive oil. Add two fried eggs* on top + $2.00</p></div>
    <div class="item"><h4>Burrito<b>5.25</b></h4><p>Choose between a sausage, egg, &amp; cheese Bacon, egg, &amp; cheese or Burrito of the Day</p></div>
    <div class="item"><h4>Scones<b>3.50</b></h4><p>Homemade right here with Kansas flour and fresh ingredients.</p></div>
    <div class="item"><h4>Yogurt Parfait<b>6.25</b></h4><p>Yogurt layered with berries topped with homemade granola.</p></div>
  </div>

  <div class="abs" style="left:16px;top:260px;width:104px;height:66px;background:var(--white)"></div>
  <div class="vlabel" style="left:20px;top:264px;width:12px;height:58px;font-size:7px">RIDIN SOLO</div>
  <div class="mini" style="left:40px;top:265px"><table>
    <tr><td>Bacon</td><td>1.80</td></tr><tr><td>Sausage</td><td>1.75</td></tr><tr><td>Biscuit</td><td>1.00</td></tr><tr><td>Egg</td><td>1.00</td></tr><tr><td>Toast</td><td>1.75</td></tr><tr><td>Pancake</td><td>2.00</td></tr><tr><td>Avocado Slices</td><td>2.75</td></tr><tr><td>Seasonal</td><td>3.50</td></tr>
  </table></div>

  <div class="abs" style="left:16px;top:337px;width:104px;height:62px;background:var(--aqua)"></div>
  <div class="abs" style="left:20px;top:339px;font-family:'Rye',serif;font-size:8.4px;color:var(--red)">Just Kiddin' Around</div>
  <div class="mini" style="left:23px;top:354px"><table style="width:92px">
    <tr><td>2 bacon or sausage<br>&nbsp;&nbsp;&nbsp;with toast</td><td>5.50</td></tr><tr><td>2 eggs &amp; toast</td><td>3.75</td></tr><tr><td>2 pancakes</td><td>4.50</td></tr><tr><td>Oatmeal cup</td><td>3.50</td></tr>
  </table></div>
  <p class="abs on-red" style="left:16px;top:404px;width:112px;font-size:3.9px;line-height:1.2">Please let your server know of any food allergies before ordering.<br>*Consuming raw or undercooked meats, poultry, seafood, shellfish, or eggs may increase your risk of foodborne illness, especially if you have certain medical conditions.</p>

  <div class="title-box" style="left:152px;top:112px;width:196px;height:21px;font-size:12.5px;line-height:19px">BREAKFAST PLATTERS</div>
  <div class="abs" style="left:152px;top:138px;width:196px">
    <div class="item" style="margin-bottom:6px"><h4>Hungry As Horse<b>12.25</b></h4><p>Two Pieces of Bacon or Sausage, two *eggs, fried potatoes &amp; two pieces of toast or pancakes served with homemade jelly.</p></div>
    <div class="item" style="margin-bottom:6px"><h4>Show Me The Gravy<b>7.25</b></h4><p>Homemade sausage gravy piled on top of two buttermilk biscuits. Add two fried eggs* on top + $2.00.</p></div>
    <div class="item" style="margin-bottom:6px"><h4>Stack Em' Hot<b>9.75</b></h4><p>Four homemade pancakes stacked high served with homemade fruit syrup and a choice of sausage or bacon.</p></div>
    <div class="item" style="margin-bottom:6px"><h4>French on The Plains<b>10.75</b></h4><p>Two pieces of French Toast served with organic maple syrup and Larkin Valley grass-fed butter with two pieces of sausage or bacon.</p></div>
    <div class="item"><h4>Country Omelet<b>10.25</b></h4><p>Three eggs combined with ham, cheese and choose from..... Spinach, onion, tomato, jalapenos mushrooms, green chilies</p></div>
  </div>
  <div class="title-box" style="left:152px;top:291px;width:196px;height:21px;font-size:12.5px;line-height:19px">BREAKFAST BOWLS</div>
  <div class="abs" style="left:152px;top:317px;width:196px">
    <div class="item" style="margin-bottom:6px"><h4>Farmer's Bowl<b>10.75</b></h4><p>Bacon, scrambled eggs*, onion, cheese and avocado served on top of a bed of fried potatoes with a choice of Red Mesa hot sauce.</p></div>
    <div class="item" style="margin-bottom:6px"><h4>Cowboy Bowl<b>12.75</b></h4><p>Prairie Lantern sirloin steak morsels served with red onion, avocado, tomato on top of a bed of fried potatoes topped with a fried egg</p></div>
    <div class="item" style="margin-bottom:6px"><h4>Veggie Bowl<b>10.25</b></h4><p>Sauteed Spinach, mushrooms, onions, tomatoes, scrambled eggs &amp; cheese served on top of a bed of fried potatoes.</p></div>
    <div class="item"><h4>Kansas Oats Bowl<b>7.25</b></h4><p>Organic Plainsview Mills oatmeal topped with fruit of the day sweetened with local honey.</p></div>
  </div>
  <div class="footer footer--dark">118 N. DEPOT ST, LARKIN, KS 67900 <span class="sep">|</span> <span class="phone">(620) 555-0148</span> <span class="sep">|</span> <span style="color:var(--aqua)">PRAIRIELANTERNPANTRY.COM</span></div>
</section>

<!-- Lunch & supper page -->
<section class="page page--lunch">
  <svg class="wave" viewBox="0 0 358 90" aria-hidden="true">
    <path d="M0 0H358V52C300 34 240 18 170 22C100 26 50 40 0 58Z" fill="var(--white)"/>
    <path d="M0 58C50 40 100 26 170 22C120 30 60 42 0 66Z" fill="var(--aqua)"/>
    <path d="M260 24C300 28 330 40 358 52V60C330 46 300 34 260 24Z" fill="var(--red)"/>
  </svg>
  <div class="brand" style="left:262px;top:6px">Prairie Lantern Pantry</div>
  <div class="abs" style="left:21px;top:57px;width:154px;height:31px;background:var(--aqua);text-align:center;padding-top:3px">
    <div style="font-family:'Graduate',serif;font-size:11px">SANDWICHES &amp; MORE</div>
    <div style="font-family:'Montserrat',sans-serif;font-weight:700;font-size:6.4px">includes choice of side</div>
  </div>
  <div class="abs on-dark" style="left:21px;top:97px;width:160px">
    <div class="item"><h4>The Prairie Chicken Fry<b>12.75</b></h4><p>Prairie Lantern beef patty served on a brioche bun with your choice of toppings. Green Chilies +.50 Mushrooms +.50 Avocado +2.75 Fried Egg* +$1.50 Bacon +2.25</p></div>
    <div class="item"><h4>The Philly<b>12.75</b></h4><p>Prairie Lantern beef patty served on a brioche bun with your choice of toppings. Green Chilies +.50 Mushrooms +.50 Avocado +2.75 Fried Egg* +$1.50 Bacon +2.25</p></div>
    <div class="item"><h4>Monte Cristo<b>11.50</b></h4><p>Three pieces of ham layered with two pieces of swiss fried between two pieces of french toast topped with powdered sugar served with raspberry jam on the side.</p></div>
    <div class="item"><h4>Grilled Sandwich Melt<b>9.50</b></h4><p>Choose between sliced roast beef, ham, or turkey piled with your choice of cheese grilled to perfection.</p></div>
    <div class="item"><h4>Prairie Club Sandwich<b>10.25</b></h4><p>Bacon, ham, and turkey stacked between pieces of jalapeno jack cheese, lettuce, and tomato on three pieces of Texas Toast.</p></div>
    <div class="item"><h4>Prairie Ranch Steak Fries<b>12.25</b></h4><p>Prairie Lantern steak served on a bed of hand cut fries topped with cheddar cheese and a side of Prairie sauce.</p></div>
    <div class="item"><h4>Prairie Steak &amp; Bacon<br>Mac 'n Cheese<b>13.75</b></h4><p>Prairie Lantern steak and bacon served on top of home made mac 'n cheese topped with cheddar cheese and side of Ranch.</p></div>
    <div class="item"><h4>Buffalo Chicken Mac 'n Cheese<b>11.50</b></h4><p>Prairie Lantern all-natural lightly hand breaded chicken sliced on a warm pile of homemade mac 'n cheese topped with buffalo sauce and ranch dressing. Make it a Wrap</p></div>
  </div>
  <div class="photo" style="left:198px;top:93px;width:74px;height:74px;background:radial-gradient(circle at 45% 45%,#8a4b2a,#3c2418 70%,#2a5aa8)" role="img" aria-label="Photo of a sandwich with ribs on a checkered paper"></div>
  <div class="photo" style="left:262px;top:137px;width:76px;height:76px;background:radial-gradient(circle at 50% 50%,#a7b04a,#5b3a22 70%)" role="img" aria-label="Photo of a Philly steak sandwich with peppers"></div>

  <div class="abs" style="left:186px;top:231px;width:160px;height:131px;background:var(--red)"></div>
  <div class="title-box" style="left:194px;top:240px;width:144px;height:19px;font-size:9.4px;line-height:17px;border-color:var(--ink)">PRAIRIE PLATES</div>
  <div class="abs on-red" style="left:194px;top:265px;width:148px">
    <div class="item"><h4>Chicken Fried Steak<b>13.85</b></h4><p>Prairie Lantern hand breaded chicken fried steak served with homemade clumpy mashed potatoes with country gravy and a side salad.</p></div>
    <div class="item"><h4>Chicken Fried Chicken<b>13.25</b></h4><p>Prairie Lantern hand breaded white chicken breast served with homemade clumpy mashed potatoes with country gravy and a side salad.</p></div>
    <div class="item"><h4>Prairie Hamburger Steak<b>12.50</b></h4><p>A PL ground beef patty topped with your choice of white or brown gravy served with mashed potatoes.</p></div>
  </div>

  <div class="abs" style="left:18px;top:372px;width:328px;height:66px;background:var(--aqua)"></div>
  <div class="abs" style="left:26px;top:377px;font-family:'Montserrat',sans-serif;font-weight:800;font-size:10px;color:var(--red)">APPETIZERS</div>
  <div class="abs" style="left:26px;top:394px;width:180px;font-family:'Montserrat',sans-serif;font-weight:700;font-size:5.2px;line-height:1.45">
    Deep Fried Cheese Curds $ 7.50 <span style="color:var(--red)">|</span> Fried Mushrooms: $8.50 <span style="color:var(--red)">|</span><br>
    Prairie Cheese Fries $8.50 <span style="color:var(--red)">|</span> Spears: $7.50 <span style="color:var(--red)">|</span><br>
    Prairie Jalapeno Poppers: $6.50 <span style="color:var(--red)">|</span><br>
    Loaded Nachos -Choose Steak or Chicken $12.50
  </div>
  <div class="abs" style="left:214px;top:378px;width:126px;height:55px;background:var(--white);border:1.2px solid var(--red)"></div>
  <div class="abs" style="left:219px;top:380px;font-family:'Rye',serif;font-size:7px;color:var(--red)">Kiddie Lunch <span style="font-size:4px">(Includes one side)</span></div>
  <div class="mini" style="left:219px;top:392px"><table style="width:112px">
    <tr><td>Grilled Cheese</td><td>5.25</td></tr><tr><td>PB &amp; J</td><td>4.50</td></tr><tr><td>Hamburger</td><td>6.50</td></tr><tr><td>Cheese Burger</td><td>7.25</td></tr>
  </table></div>
  <div class="footer footer--light">118 N. DEPOT ST, LARKIN, KS 67900 <span class="sep">|</span> <span class="phone">(620) 555-0148</span> <span class="sep">|</span> PRAIRIELANTERNPANTRY.COM</div>
</section>

<!-- Burgers & salads page -->
<section class="page page--burgers">
  <svg class="wave" viewBox="0 0 358 90" aria-hidden="true">
    <path d="M0 0H358V22C290 14 230 12 170 18C100 24 40 30 0 32Z" fill="var(--white)"/>
    <path d="M0 32C40 30 100 24 170 18C120 26 60 34 0 39Z" fill="var(--aqua)"/>
    <path d="M230 14C280 11 320 16 358 22V30C320 22 280 16 230 14Z" fill="var(--red)"/>
  </svg>
  <div class="brand" style="left:260px;top:8px">Prairie Lantern Pantry</div>
  <div class="burger-heading">
    <div style="font-size:11.4px;color:var(--aqua)">PRAIRIE <span style="color:var(--red)">BURGERS</span></div>
    <div style="font-size:8.6px;color:var(--white);margin-left:42px;margin-top:1px">WITH ONE SIDE</div>
  </div>
  <div class="abs on-dark" style="left:14px;top:72px;width:166px">
    <div class="item" style="margin-bottom:2px"><h4 style="color:var(--aqua)">Call It Your Own<b style="color:var(--white)">11.25</b></h4><p>Prairie Lantern beef patty served on a brioche bun with your choice of toppings. Green Chilies +.50 Mushrooms +.50 Avocado +2.75 Fried Egg* +$1.50 Bacon +2.25</p></div>
    <div class="item" style="margin-bottom:2px"><h4 style="color:var(--aqua)">The Sam<b style="color:var(--white)">12.25</b></h4><p>A Prairie Lantern patty with bacon pieces, sauteed onions, jalapeno cheese &amp; a homemade spicy sauce on top a brioche bun.</p></div>
    <div class="item" style="margin-bottom:2px"><h4 style="color:var(--aqua)">The Swiss<b style="color:var(--white)">11.75</b></h4><p>A Prairie Lantern patty topped with mushrooms &amp; Swiss served with a brioche bun.</p></div>
    <div class="item" style="margin-bottom:2px"><h4 style="color:var(--aqua)">The Prairie<b style="color:var(--white)">11.50</b></h4><p>A Prairie Lantern patty topped with green chilies &amp; Pepper Jack cheese served on a brioche bun.</p></div>
    <div class="item" style="margin-bottom:2px"><h4 style="color:var(--aqua)">The Diamond Back<b style="color:var(--white)">12.25</b></h4><p>A Prairie Lantern patty topped with a slice of ham, cheese, and BBQ sauce served on Texas Toast.</p></div>
    <div class="item" style="margin-bottom:2px"><h4 style="color:var(--aqua)">It's Not Beef<b style="color:var(--white)">12.25</b></h4><p>A Prairie Lantern chicken fried chicken breast topped with American on a brioche bun.</p></div>
  </div>
  <div class="abs on-dark" style="left:188px;top:93px;width:163px">
    <div class="item" style="margin-bottom:2px"><h4 style="color:var(--aqua)">Jalapeno Popper Burger<b style="color:var(--white)">12.75</b></h4><p>Pure Beef patty topped with jalapeno cream cheese &amp; bacon.</p></div>
    <div class="item" style="margin-bottom:2px"><h4 style="color:var(--aqua)">Prairie Guacamole Burger<b style="color:var(--white)">12.99</b></h4><p>Pure Beef patty topped with homemade PL guacamole.</p></div>
    <div class="item" style="margin-bottom:2px"><h4 style="color:var(--aqua)">Smothered Open-Face Burger<b style="color:var(--white)">12.75</b></h4><p>Pure Beef patty topped with homemade mashed potatoes served on top of Texas Toast with your choice of white or brown gravy.</p></div>
    <div class="item" style="margin-bottom:2px"><h4 style="color:var(--aqua)">Bacon Jam Bacon Burger<b style="color:var(--white)">12.50</b></h4><p>Pure Beef patty topped with spicy bacon jam &amp; bacon.</p></div>
    <div class="item" style="margin-bottom:2px"><h4 style="color:var(--aqua)">Double Bacon Cheeseburger<b style="color:var(--white)">15.25</b></h4><p>Two pure beef patties topped with two pieces of bacon and choice toppings.</p></div>
    <div class="item"><h4 style="color:var(--aqua)">Prairie Smash Burger<b style="color:var(--white)">10.50</b></h4><p>Pure beef patty perfectly seared and smashed to a thinner, juicy patty. Your choice of toppings.</p></div>
  </div>

  <div class="abs" style="left:14px;top:224px;width:161px;height:208px;background:var(--aqua)"></div>
  <div class="abs" style="left:20px;top:224px;font-family:'Lobster',cursive;font-size:20px;color:var(--red)">Salads</div>
  <div class="abs" style="left:92px;top:228px;width:80px;font-family:'Montserrat',sans-serif;font-weight:700;font-size:4.8px;line-height:1.2">(Make any of our Salads into a Wrap Plus a Bag of Chips)</div>
  <div class="abs" style="left:20px;top:250px;width:152px">
    <div class="item" style="margin-bottom:3px"><h4>Prairie Steak Salad<b>13.75</b></h4><p>Prairie Lantern all-natural, pasture raised &amp; finished sirloin steak served on a bed of greens with feta, tomatoes, cucumbers, avocado and red onion with choice dressing.</p></div>
    <div class="item" style="margin-bottom:3px"><h4>Grilled Chicken Pecan Feta<b>12.75</b></h4><h4>Cranberry Salad</h4><p>A grilled all-natural PL chicken breast grilled and sliced over a bed of greens topped with feta cheese, pecans, diced cucumbers, red onion and dried cranberries served with a tart Raspberry Vinaigrette.</p></div>
    <div class="item" style="margin-bottom:3px"><h4>Prairie Chef Salad<b>10.50</b></h4><p>Mixed greens full of cut veggies, shredded cheese topped with ham.</p></div>
    <div class="item" style="margin-bottom:3px"><h4>Veggie Salad<b>9.50</b></h4><p>Mixed greens full of cut veggies, feta, and kalamata olives with your choice of dressing.</p></div>
    <div class="item"><h4>Buffalo Chicken Salad<b>12.75</b></h4><p>A lightly hand breaded PL all-natural chicken breast fried and sliced to perfection laid over a bowl of greens with diced cucumbers, chopped celery, shredded carrots, red onion, and feta cheese topped with mild Buffalo sauce &amp; Ranch dressing</p></div>
  </div>

  <div class="photo" style="left:226px;top:225px;width:70px;height:70px;background:radial-gradient(circle at 50% 50%,#c98a3c,#6d4a2a 70%)" role="img" aria-label="Photo of a fried chicken sandwich"></div>
  <div class="photo" style="left:187px;top:281px;width:70px;height:70px;background:radial-gradient(circle at 50% 50%,#b58a45,var(--photo-green) 70%)" role="img" aria-label="Photo of a chicken salad bowl"></div>
  <div class="photo" style="left:277px;top:283px;width:70px;height:70px;background:radial-gradient(circle at 50% 50%,#8c3b32,#4d3a2a 70%)" role="img" aria-label="Photo of sliced steak salad"></div>

  <div class="abs" style="left:188px;top:367px;width:157px;height:63px;background:var(--white)"></div>
  <div class="vlabel" style="left:191px;top:370px;width:14px;height:57px;font-size:7px">SIDES</div>
  <div class="mini" style="left:208px;top:371px"><table>
    <tr><td>Handcut Fries</td><td>3.75</td></tr><tr><td>Greek Pasta</td><td>3.75</td></tr><tr><td>Side Salad</td><td>3.00</td></tr><tr><td>Gma's Potato</td><td>3.00</td></tr><tr><td>Salas</td><td></td></tr><tr><td>Homemac Mac</td><td>4.25</td></tr><tr><td>Chips</td><td>2.50</td></tr>
  </table></div>
  <div class="vlabel" style="left:272px;top:370px;width:14px;height:57px;font-size:7px;background:var(--aqua);color:var(--ink)">EXTRAS</div>
  <div class="mini" style="left:290px;top:371px"><table>
    <tr><td>Add a Patty</td><td>5.00</td></tr><tr><td>Fried Egg</td><td>1.50</td></tr><tr><td>Cheese</td><td>0.75</td></tr><tr><td>Avocado</td><td>2.75</td></tr><tr><td>Green</td><td>0.50</td></tr><tr><td>Jalapenos</td><td>0.50</td></tr><tr><td>Gravy</td><td>1.00</td></tr>
  </table></div>
  <div class="footer footer--light">118 N. DEPOT ST, LARKIN, KS 67900 <span class="sep">|</span> <span class="phone">(620) 555-0148</span> <span class="sep">|</span> PRAIRIELANTERNPANTRY.COM</div>
</section>

<!-- Drinks & dessert page -->
<section class="page page--drinks">
  <svg class="wave" viewBox="0 0 358 90" aria-hidden="true">
    <path d="M0 0H358V30C300 22 240 22 170 30C100 38 50 40 0 40Z" fill="var(--white)"/>
    <path d="M0 40C50 40 100 38 170 30C110 42 50 46 0 48Z" fill="var(--ink)"/>
    <path d="M200 26C260 18 320 24 358 32V42C320 32 260 24 200 26Z" fill="var(--red)"/>
  </svg>
  <div class="brand" style="left:22px;top:8px">Prairie Lantern Pantry</div>
  <div class="photo" style="left:134px;top:52px;width:42px;height:42px;border:none;background:radial-gradient(circle,#d9b993,#8a5a36 60%,#f3f3f3 62%)" role="img" aria-label="Photo of a latte from above"></div>
  <div class="abs drink-list" style="left:195px;top:47px;width:74px;font-size:5.6px">
    <div class="row"><span>COFFEE**</span><span>2.50</span></div>
    <div class="row"><span>ICED TEA**</span><span>2.25</span></div>
    <div class="row"><span>MILK</span><span>2.75</span></div>
    <div class="row"><span>JUICE</span><span>3.00</span></div>
    <div class="row"><span>SODA**</span><span>2.89</span></div>
  </div>
  <div class="abs" style="left:283px;top:78px;font-family:'Montserrat',sans-serif;font-weight:700;font-size:4.6px">** FREE Refills</div>

  <div class="abs" style="left:14px;top:109px;width:161px;height:226px;background:var(--ink)"></div>
  <div class="title-box" style="left:31px;top:98px;width:144px;height:26px;border:1.5px solid var(--ink);padding-top:2px">
    <div style="font-size:11px;line-height:1">ESPRESSO BAR</div>
    <div style="font-family:'Montserrat',sans-serif;font-weight:700;font-size:5.6px">16 OZ. HOT, ICED, OR FRAPPE</div>
  </div>
  <div class="abs drink-list" style="left:20px;top:130px;width:130px;color:var(--white)">
    <div class="row"><span>CARAMEL MACCHIATO</span><span>$4.65</span></div>
    <div class="row"><span>WHITE CHOCOLATE MOCHA</span><span>$4.65</span></div>
    <div class="row"><span>CAFE MOCHA</span><span>$4.65</span></div>
    <div class="row"><span>HOT CHOCOLATE</span><span>$3.50</span></div>
    <div class="row"><span>GOURMET HOT CHOCOLATE</span><span>$4.50</span></div>
    <div class="row"><span>CHAI TEA LATTE</span><span>$4.75</span></div>
    <div class="row"><span>MATCHA LATTE (GREEN TEA)</span><span>$4.75</span></div>
    <div class="row"><span>CAFE LATTES &amp; CAPPUCCINOS</span><span>$3.85</span></div>
    <div class="row"><span>ADD FLAVORINGS PER PUMP</span><span>$0.50</span></div>
    <div style="color:var(--red)">PUMPKIN SPICE, COCONUT, PEPPERMINT, HAZELNUT, IRISH CREAM, VANILLA (SF) CHOC CHIP COOKIE DOUGH SALTED CARAMEL (SF), TOASTED MARSHMALLOW, WHITE CHOCOLATE</div>
    <div class="row"><span>EXTRA ESPRESSO SHOT</span><span>$1.00</span></div>
    <div class="row"><span>DRIP COFFEE</span><span>$2.65</span></div>
    <div class="row"><span>ICED COFFEE (VANILLA OR CARAMEL)</span><span>$3.00</span></div>
    <div class="row"><span>HOT TEA LOOSE LEAF</span><span>$2.85</span></div>
    <div style="color:var(--red)">COTTAGE BREAKFAST, EARL GREY, HAPPY GREEN, WHITE JASMINE, WHITE COCONUT CREME, EGYPTIAN CHAMOMILE, HIBISCUS TWIST HERBAL</div>
    <div class="row"><span>AMERICANO</span><span>$3.50</span></div>
    <div class="row"><span>CUBANO</span><span>$4.50</span></div>
    <div>(ESPRESSO, CREAM, &amp; BROWN SUGAR)</div>
  </div>

  <div class="abs" style="left:184px;top:109px;width:161px;height:226px;background:var(--red)"></div>
  <div class="title-box" style="left:196px;top:98px;width:132px;height:27px;border:1.5px solid var(--ink);padding-top:2px">
    <div style="font-size:11px;line-height:1">SODA FOUNTAIN</div>
    <div style="font-family:'Montserrat',sans-serif;font-weight:700;font-size:5.6px">24 oz</div>
  </div>
  <div class="abs drink-list" style="left:194px;top:129px;width:144px;color:var(--white)">
    <div class="row"><span>SODA</span><span>$2.89</span></div>
    <div style="padding-left:6px">COLA, PEPPER SPICE, ROOT BEER, LIME RICKEY</div>
    <div style="height:6px"></div>
    <div class="row"><span>CHERRY VANILLA COLA</span><span>$3.25</span></div>
    <div class="row"><span>STRAWBERRY VANILLA PEPPER SPICE</span><span>$3.50</span></div>
    <div class="row"><span>VANILLA CREME ROOT BEER</span><span>$3.50</span></div>
    <div class="row"><span>LIMEADE or LEMONADE</span><span>$3.00</span></div>
    <div class="row"><span>CHERRY or STRAWBERRY LIMEADE</span><span>$3.50</span></div>
    <div class="row"><span>FRESH CUCUMBER MINT LIMEADE</span><span>$3.65</span></div>
    <div class="row"><span>BRAZILIAN CHERRY LIMEADE</span><span>$3.75</span></div>
    <div class="row"><span>FRESH PEACH LIMEADE</span><span>$3.50</span></div>
    <div style="height:6px"></div>
    <div class="row"><span>ICE CREAM</span><span>$3.75</span></div>
    <div>(Choc, Vanilla, Strawberry)<br>2 Scoops</div>
    <div class="row"><span>CHOCOLATE SODA</span><span>$3.95</span></div>
    <div class="row"><span>ICE CREAM SUNDAE</span><span>$4.50</span></div>
    <div>Toppings:<br>Choc, Fudge, Strawberry, Caramel</div>
    <div class="row"><span>FLOATS</span><span>$3.95</span></div>
    <div class="row"><span>SHAKES</span><span>$4.75</span></div>
    <div class="row"><span>MALTS</span><span>$4.85</span></div>
  </div>
  <div class="abs" style="left:230px;top:297px;width:86px;height:38px;background:linear-gradient(90deg,#8a1f1a,#f4f4f4 40%,#f2c24a 70%,#e8742a)" role="img" aria-label="Photo of fountain drinks, a sundae and shakes"></div>

  <div class="abs" style="left:0;top:337px;width:358px;height:106px;background:var(--white)"></div>
  <div class="abs" style="left:20px;top:344px;width:132px;height:74px;transform:rotate(-4deg);background:var(--red)"></div>
  <div class="abs" style="left:40px;top:348px;width:106px;height:64px;transform:rotate(-4deg);background:linear-gradient(135deg,#c4b49a,#6f6a5e);border:2px solid var(--white)" role="img" aria-label="Photo of the owners seated in a truck"></div>
  <div class="story-label">OUR STORY</div>
  <div class="abs" style="left:164px;top:361px;font-family:'Montserrat',sans-serif;font-weight:700;font-size:6px;color:var(--teal-text)">MEET DALE &amp; RENEE HARLAN</div>
  <p class="abs" style="left:164px;top:373px;width:182px;font-size:5px;line-height:1.2">Dale &amp; Renee were both a part of a 42,000 head feed yard in western Kansas years ago. Grain-fed beef was the only kind of beef we had eaten. Any mention of grass-fed beef and our eyes will roll. Little did we know God has other plan and soon regenerative farming &amp; ranching would be the heart of our operations. Grass-fed and finished meats are not only healthier than grain-fed but the process of animals grazing on open pastures benefit the crops, soils &amp; environment.</p>
  <div class="footer footer--dark">118 N. DEPOT ST, LARKIN, KS 67900 <span class="sep">|</span> <span class="phone">(620) 555-0148</span> <span class="sep">|</span> PRAIRIELANTERNPANTRY.COM</div>
</section>

</body>
</html>
```